Free offer card

I need a business card sized FREE CLASS offer thing....Our target market is 18-40 year old women. We are the "sexy" pole studio but don't want to scare people off. This card will be given out by students and staff when they meet people that are interested and also put in hair dressers and sports shops etc. I've got HEAPS of photos so I'll upload a few, I'll also upload the last brochure we did but I'm not sure it's really doing it's job....might be a little scary? The free trial class maybe wasn't clear enough. I think maybe free class instead of using the word "trial" so they don't think they are going to get a hard sell. Need a space we can write student/teachers name on it...maybe Marla's Muse_________
And need both studios details on it (on attached brochure) happy to send different photos if it helps
I can get high res stuff and better copies of the fit fierce sexy brochure if you want...haven't used this website before not really sure what you need

```html
<!DOCTYPE html>
<html lang="en">
<head>
<meta charset="utf-8">
<title>Marla's Pole Studio – Free Class Card</title>
<link rel="stylesheet" href="https://fonts.googleapis.com/css2?family=Exo+2:wght@700;800&family=Kaushan+Script&family=Source+Sans+3:wght@400&display=swap">
<style>
  :root {
    --backdrop: #cccccc;
    --card: #ffffff;
    --sky: #cfe8f6;
    --blush: #f6d3e4;
    --magenta: #e0117f;
    --ink: #1a1a1a;
    --photo-light: #f6e4ef;
    --photo-mid: #f2d2e3;
    --photo-rim: #e6e2f3;
  }
  * { margin: 0; padding: 0; box-sizing: border-box; }
  html, body { width: 1200px; height: 1200px; overflow: hidden; background: var(--backdrop); }
  .canvas { position: relative; width: 1200px; height: 1200px; }

  .card { position: absolute; top: 174px; width: 520px; height: 852px; background: var(--card); overflow: hidden; }
  .card--front { left: 42px; }
  .card--back { left: 631px; }

  .card__bands { position: absolute; inset: 0; width: 520px; height: 852px; }

  .brand {
    position: absolute; left: 0; width: 100%; top: 52px;
    text-align: center;
    font-family: "Exo 2", sans-serif; font-weight: 800;
    font-size: 40px; line-height: 1; letter-spacing: 1px;
    color: var(--magenta); text-transform: uppercase;
  }
  .card--back .brand { top: 58px; }

  .hero-photo { position: absolute; left: 32px; top: 172px; width: 460px; height: 460px; }

  .offer-title {
    position: absolute; left: 0; width: 100%; top: 646px;
    text-align: center;
    font-family: "Exo 2", sans-serif; font-weight: 800;
    font-size: 38px; line-height: 1; color: var(--magenta);
  }
  .member-label {
    position: absolute; left: 0; width: 100%; top: 714px;
    text-align: center;
    font-family: "Kaushan Script", cursive;
    font-size: 46px; line-height: 1; color: var(--ink);
  }
  .name-field {
    position: absolute; left: 34px; top: 776px; width: 452px; height: 59px;
    background: var(--card); border-radius: 30px;
  }

  .studio { position: absolute; left: 0; width: 100%; text-align: center; }
  .studio--city { top: 212px; }
  .studio--miranda { top: 452px; }
  .studio__name {
    font-family: "Exo 2", sans-serif; font-weight: 700;
    font-size: 35px; line-height: 38px; color: var(--ink);
  }
  .studio__rule { width: 227px; height: 4px; background: var(--magenta); margin: 16px auto 18px; }
  .studio__details {
    font-family: "Source Sans 3", sans-serif; font-weight: 400;
    font-size: 32px; line-height: 40px; letter-spacing: 1.5px; color: var(--ink);
  }

  .contact { position: absolute; left: 0; width: 100%; text-align: center; font-family: "Source Sans 3", sans-serif; color: var(--ink); }
  .contact--email { top: 742px; font-size: 30px; letter-spacing: 1px; }
  .contact--web { top: 796px; font-size: 26px; letter-spacing: 0.5px; }
</style>
</head>
<body>
<main class="canvas">

  <section class="card card--front" aria-label="Free class voucher, front">
    <svg class="card__bands" viewBox="0 0 520 852" aria-hidden="true">
      <path d="M0 0 H520 V138 Q260 178 0 138 Z" fill="var(--sky)"/>
      <path d="M0 722 Q260 678 520 722 V852 H0 Z" fill="var(--blush)"/>
    </svg>
    <div class="brand">Marla's Pole Studio</div>
    <svg class="hero-photo" viewBox="0 0 460 460" role="img" aria-label="Photo of a pole dancer performing an inverted pose on a pole">
      <defs>
        <radialGradient id="photoGlow" cx="50%" cy="50%" r="50%">
          <stop offset="0%" stop-color="var(--photo-light)"/>
          <stop offset="85%" stop-color="var(--photo-mid)"/>
          <stop offset="100%" stop-color="var(--photo-rim)"/>
        </radialGradient>
      </defs>
      <circle cx="230" cy="230" r="230" fill="url(#photoGlow)"/>
    </svg>
    <h1 class="offer-title">FREE CLASS VAUCHER</h1>
    <div class="member-label">Marla's Muse</div>
    <div class="name-field" aria-label="Space for student or teacher name"></div>
  </section>

  <section class="card card--back" aria-label="Studio details, back">
    <svg class="card__bands" viewBox="0 0 520 852" aria-hidden="true">
      <path d="M0 0 H520 V146 Q260 188 0 146 Z" fill="var(--sky)"/>
      <path d="M0 731 Q260 686 520 731 V852 H0 Z" fill="var(--blush)"/>
    </svg>
    <div class="brand">Marla's Pole Studio</div>

    <div class="studio studio--city">
      <h2 class="studio__name">CITY STUDIO</h2>
      <div class="studio__rule"></div>
      <p class="studio__details">Level 2, 118 Harbour Lane,<br>Sydney NSW 2000<br>(02) 9000-4172</p>
    </div>

    <div class="studio studio--miranda">
      <h2 class="studio__name">MIRANDA STUDIO</h2>
      <div class="studio__rule"></div>
      <p class="studio__details">5/42 Bayview Pde,<br>Miranda NSW 2228<br>(02) 9000-6851</p>
    </div>

    <p class="contact contact--email">info@marlaspolestudio.com.au</p>
    <p class="contact contact--web">WWW.MARLASPOLESTUDIO.COM.AU</p>
  </section>

</main>
</body>
</html>
```